Mental Health care Company in Washington DC

We are a new mental health care services provider in Washington DC. Please look at these sites.
https://marlowbrookpartners.com
https://www.quillstoneinc.com
https://velmarsh-kt.org/
https://www.trivanqx.com
https://www.thelanternofqz.com

```html
<!DOCTYPE html>
<html lang="en">
<head>
<meta charset="utf-8">
<title>Velora Health Services – Mental Health Care in Washington</title>
<link rel="stylesheet" href="https://fonts.googleapis.com/css2?family=Lexend:wght@400;500;600&family=Poppins:wght@400;500;600&display=swap">
<style>
:root{
  --orange:#f47c20;
  --navy:#0f2a4a;
  --teal:#a6dbdc;
  --teal-soft:#e8f6f6;
  --teal-btn:#9fdadb;
  --peach:#fde8d8;
  --peach-soft:#fdf3ec;
  --cream:#f8f7f1;
  --text:#3c4656;
  --white:#ffffff;
}
*{margin:0;padding:0;box-sizing:border-box}
html,body{width:1200px;height:3413px;overflow:hidden;background:var(--white)}
body{position:relative;font-family:"Poppins",sans-serif;color:var(--text)}
.abs{position:absolute}
h1,h2,h3,h4{font-family:"Lexend",sans-serif;color:var(--navy);font-weight:500}
.btn{position:absolute;display:flex;align-items:center;justify-content:space-between;gap:12px;height:42px;padding:0 18px 0 20px;border-radius:21px;font-size:13px;font-weight:600;color:var(--white);background:var(--orange);text-decoration:none;white-space:nowrap}
.btn svg{width:14px;height:14px;flex:none}
.btn.teal{background:var(--teal-btn)}
.btn.ghost{background:transparent;border:1.5px solid var(--navy);color:var(--navy)}
.btn.white{background:var(--white);color:var(--navy)}
.eyebrow{font-size:14px;color:var(--orange);display:flex;align-items:center;gap:6px}
.eyebrow::after{content:"";width:70px;height:1px;background:var(--orange)}

/* header */
.site-header{position:absolute;top:0;left:0;width:1200px;height:80px;background:var(--white)}
.brand{position:absolute;left:122px;top:18px;width:180px;display:flex;align-items:center;gap:8px;font-family:"Lexend",sans-serif;font-size:18px;line-height:21px;font-weight:500;color:var(--navy)}
.brand .dot{width:12px;height:12px;border-radius:50%;background:var(--orange);flex:none}
.nav{position:absolute;left:320px;top:30px;display:flex;gap:23px;font-size:13px;color:var(--navy);white-space:nowrap}
.header-cta{left:810px;top:21px;height:36px;font-size:12px;padding:0 14px;gap:8px}
.icon-btn{position:absolute;top:27px;width:22px;height:22px;border:1.3px solid var(--navy);border-radius:50%}

/* hero */
.hero-photo{position:absolute;left:0;top:80px;width:1200px;height:598px;background:linear-gradient(90deg,#efe9e2 0%,#ead9c6 40%,#c8a47d 62%,#8f9b5a 85%,#6f8a3e 100%)}
.hero-eyebrow{left:119px;top:235px}
.hero h1{position:absolute;left:119px;top:253px;font-size:47px;line-height:56px;font-weight:600}
.hero-sub{position:absolute;left:121px;top:368px;font-family:"Lexend",sans-serif;font-size:21px;color:var(--navy)}

/* services */
.section-title{position:absolute;left:0;width:1200px;text-align:center;font-size:32px;font-weight:500}
.service-card{position:absolute;top:788px;width:220px;height:250px;background:var(--teal-soft);border-radius:110px 110px 0 0;text-align:center}
.service-card .ill{width:80px;height:60px;margin:32px auto 0;border-radius:30px;background:linear-gradient(135deg,var(--orange),var(--teal))}
.service-card h3{font-size:15px;line-height:18px;margin-top:14px;font-weight:500}
.service-card p{font-size:10.5px;line-height:17px;margin:10px 20px 0}
.arrow-circle{position:absolute;width:20px;height:20px;border:1.3px solid var(--navy);border-radius:50%;display:flex;align-items:center;justify-content:center}
.arrow-circle svg{width:10px;height:10px}

.band-pattern{position:absolute;left:0;top:1123px;width:1200px;height:62px;background:linear-gradient(180deg,#fdf3ef,#fbe6de 50%,#fdf3ef)}

/* about */
.about{position:absolute;left:0;top:1188px;width:1200px;height:484px;background:var(--cream)}
.about-photo{position:absolute;left:0;top:0;width:720px;height:484px;background:linear-gradient(120deg,#c9b59d 0%,#b8c6bd 45%,#e6e1d6 100%)}
.about-card{position:absolute;left:653px;top:61px;width:427px;height:367px;background:var(--peach);padding:36px 42px}
.about-card h2{font-size:29px;line-height:37px;margin-top:6px;white-space:nowrap}
.about-card p{font-size:11px;line-height:18px;margin-top:10px}

/* why */
.why{position:absolute;left:0;top:1672px;width:1200px;height:434px;background:var(--teal)}
.why-ill{position:absolute;left:180px;top:64px;width:235px;height:320px;border-radius:120px 120px 40px 40px;background:linear-gradient(180deg,#bfe4e4,#9fd4d5)}
.why h2{position:absolute;left:120px;top:200px;font-size:35px;line-height:40px;color:var(--white);font-weight:600}
.why-item{position:absolute;width:220px;color:var(--white)}
.why-item h4{font-size:17px;color:var(--white);font-weight:400;display:flex;gap:8px;align-items:flex-start;line-height:20px}
.why-item h4 svg{flex:none;width:15px;height:15px;margin-top:3px}
.why-item p{font-size:10.5px;line-height:16px;margin:4px 0 0 30px;color:#f4fbfb}

/* focus / promise */
.split{position:absolute;top:2106px;width:600px;height:321px}
.split.focus{left:0;background:var(--peach-soft)}
.split.promise{left:600px;background:var(--teal-soft)}
.oval-photo{position:absolute;top:50px;width:166px;height:244px;border-radius:83px;border:4px solid var(--white);box-shadow:0 0 0 1px #e4e4e4}
.split h3{position:absolute;font-size:19px;font-weight:500}
.split p{position:absolute;font-size:11.5px;line-height:18px;width:260px}

/* approach */
.approach-card{position:absolute;top:2540px;width:227px;height:228px;background:var(--teal-soft)}
.approach-card .photo{position:absolute;left:5px;top:6px;width:217px;height:172px}
.approach-card h4{position:absolute;left:0;top:204px;width:100%;text-align:center;font-size:15px;font-weight:500}

/* cta + footer */
.cta-pattern{position:absolute;left:0;top:2960px;width:1200px;height:70px;background:linear-gradient(180deg,#fdf3ef,#fbe6de)}
.footer{position:absolute;left:0;top:3030px;width:1200px;height:383px;background:var(--navy);color:var(--white)}
.cta{position:absolute;left:197px;top:2897px;width:806px;height:222px;background:var(--orange);text-align:center}
.cta h2{color:var(--white);font-size:33px;margin-top:60px;font-weight:500}
.cta p{font-size:11.5px;line-height:15px;color:var(--white);margin-top:6px}
.footer-col{position:absolute;top:129px}
.footer-col h4{color:var(--white);font-size:15px;font-weight:500;margin-bottom:18px}
.footer-col ul{list-style:none;font-size:10px;line-height:22px}
.footer .divider{position:absolute;top:125px;width:1px;height:212px;background:#2d4566}
.contact-row{display:flex;gap:10px;font-size:9.5px;line-height:12px;margin-bottom:14px;align-items:center}
.contact-row .ic{width:22px;height:22px;border:1px solid var(--white);border-radius:50%;flex:none;display:flex;align-items:center;justify-content:center}
.contact-row svg{width:11px;height:11px}
.social{width:22px;height:22px;border:1px solid var(--white);border-radius:50%;display:inline-block;margin-right:8px}
.field{width:166px;height:36px;border:1px solid var(--white);border-radius:18px;font-size:9.5px;padding:11px 16px}
</style>
</head>
<body>

<header class="site-header">
  <div class="brand"><span class="dot"></span><span>Velora Health<br>Services</span></div>
  <nav class="nav"><span>About us</span><span>Therapies &amp; Treatment</span><span>Services</span><span>Gallery</span><span>Contact us</span></nav>
  <a class="btn header-cta">Schedule an Appointment <svg viewBox="0 0 14 14"><path d="M2 7h10M8 3l4 4-4 4" stroke="#fff" stroke-width="1.6" fill="none"/></svg></a>
  <span class="icon-btn" style="left:1027px"></span>
  <span class="icon-btn" style="left:1055px"></span>
</header>

<section class="hero">
  <div class="hero-photo" role="img" aria-label="Photo of a smiling woman with eyes closed among wildflowers in a sunny field"></div>
  <div class="eyebrow abs hero-eyebrow">Welcome to Velora Health Services</div>
  <h1>Empowering Minds<br>Healing Lives –</h1>
  <div class="hero-sub">Mental Health Care in Washington</div>
  <a class="btn" style="left:122px;top:420px">Find a Therapist <svg viewBox="0 0 14 14"><path d="M2 7h10M8 3l4 4-4 4" stroke="#fff" stroke-width="1.6" fill="none"/></svg></a>
  <a class="btn teal" style="left:288px;top:420px">Request a Demo <svg viewBox="0 0 14 14"><path d="M2 7h10M8 3l4 4-4 4" stroke="#fff" stroke-width="1.6" fill="none"/></svg></a>
</section>

<h2 class="section-title" style="top:728px">Services We Offer</h2>
<span class="arrow-circle" style="left:80px;top:921px"><svg viewBox="0 0 10 10"><path d="M6.5 1.5L3 5l3.5 3.5" stroke="#0f2a4a" stroke-width="1.4" fill="none"/></svg></span>
<span class="arrow-circle" style="left:1100px;top:927px"><svg viewBox="0 0 10 10"><path d="M3.5 1.5L7 5 3.5 8.5" stroke="#0f2a4a" stroke-width="1.4" fill="none"/></svg></span>

<article class="service-card" style="left:125px">
  <div class="ill" role="img" aria-label="Lotus flower illustration"></div>
  <h3>Individua<br>Therapy</h3>
  <p>The goal of individual therapy is to inspire change &amp; improve the quality of life through self awareness &amp; self-exploration</p>
</article>
<article class="service-card" style="left:370px">
  <div class="ill" role="img" aria-label="Illustration of two people side by side"></div>
  <h3>Couples and<br>Family Counseling</h3>
  <p>Couples &amp; family counseling techniques aim to improve relationships by addressing communication, conflict resolution, &amp; emotional well-being.</p>
</article>
<article class="service-card" style="left:612px">
  <div class="ill" role="img" aria-label="Illustration of a person figure"></div>
  <h3>Substance Abuse<br>Addiction Counseling</h3>
  <p>Substance abuse affects every part of your life. It can hurt you and the people around you. It can ruin relationships and your financial health.</p>
</article>
<article class="service-card" style="left:854px">
  <div class="ill" role="img" aria-label="Illustration of a child figure"></div>
  <h3>Child and<br>Adolescent Issues</h3>
  <p>Several important mental health disorders, such as depression, anxiety disorders, &amp; eating disorders, often start during childhood &amp; adolescence</p>
</article>
<a class="btn" style="left:521px;top:1065px">View All Services <svg viewBox="0 0 14 14"><path d="M2 7h10M8 3l4 4-4 4" stroke="#fff" stroke-width="1.6" fill="none"/></svg></a>

<div class="band-pattern" role="img" aria-label="Soft decorative pattern band"></div>

<section class="about">
  <div class="about-photo" role="img" aria-label="Photo of a caregiver and an older woman smiling together on a sofa, looking at a tablet"></div>
  <div class="about-card">
    <div class="eyebrow">About Us</div>
    <h2>Welcome to<br>Velora Health Services</h2>
    <p>At Velora Health Services, we are committed to providing top notch health consulting services to our clients. Our mission is to help people achieve optimal health and wellness through personalized plans and ongoing support. Our team of experienced health consultants has a diverse range of expertise, from nutrition and fitness to stress management and holistic health.</p>
    <a class="btn" style="left:44px;top:298px">Read More <svg viewBox="0 0 14 14"><path d="M2 7h10M8 3l4 4-4 4" stroke="#fff" stroke-width="1.6" fill="none"/></svg></a>
    <a class="btn ghost" style="left:182px;top:298px">Meet Our Team <svg viewBox="0 0 14 14"><path d="M2 7h10M8 3l4 4-4 4" stroke="#0f2a4a" stroke-width="1.6" fill="none"/></svg></a>
  </div>
</section>

<section class="why">
  <div class="why-ill" role="img" aria-label="Line illustration of a head in profile with a brain"></div>
  <h2>Why Choose Us<br>Velora Health<br>Services?</h2>
  <div class="why-item" style="left:486px;top:71px">
    <h4><svg viewBox="0 0 15 15"><circle cx="7.5" cy="7.5" r="7.5" fill="#fff"/><path d="M4 7.6l2.3 2.2L11 5" stroke="#a6dbdc" stroke-width="1.6" fill="none"/></svg>Assessment</h4>
    <p>In just 3–5 minutes, you'll answer some questions that can help identify areas where you might need support.</p>
  </div>
  <div class="why-item" style="left:837px;top:71px">
    <h4><svg viewBox="0 0 15 15"><circle cx="7.5" cy="7.5" r="7.5" fill="#fff"/><path d="M4 7.6l2.3 2.2L11 5" stroke="#a6dbdc" stroke-width="1.6" fill="none"/></svg>Dedicated Guidance</h4>
    <p>Meet with your Care Navigator for clinical guidance and emotional support throughout your journey.</p>
  </div>
  <div class="why-item" style="left:486px;top:260px">
    <h4><svg viewBox="0 0 15 15"><circle cx="7.5" cy="7.5" r="7.5" fill="#fff"/><path d="M4 7.6l2.3 2.2L11 5" stroke="#a6dbdc" stroke-width="1.6" fill="none"/></svg>Inclusive Care</h4>
    <p>Quickly browse and schedule appointments with the provider who best fits your needs and preferences - or get started with on-demand digital exercises.</p>
  </div>
  <div class="why-item" style="left:837px;top:260px">
    <h4><svg viewBox="0 0 15 15"><circle cx="7.5" cy="7.5" r="7.5" fill="#fff"/><path d="M4 7.6l2.3 2.2L11 5" stroke="#a6dbdc" stroke-width="1.6" fill="none"/></svg>Personalized<br>Recommendations</h4>
    <p>You'll receive a care plan based on your goals and assessment results, including a curated list of providers from our diverse network.</p>
  </div>
</section>

<section class="split focus">
  <div class="oval-photo" style="left:123px;background:linear-gradient(160deg,#8a7564,#b9a892 60%,#6e5a48)" role="img" aria-label="Photo of a therapist in session with a client in an office"></div>
  <h3 style="left:318px;top:92px">Our Treatment Focus</h3>
  <p style="left:318px;top:124px">Our focus is to help individuals heal, energize, and become aware of their inner strengths. We achieve this by providing a neutral safe space, listening to your concerns, and customizing a treatment plan.</p>
  <a class="btn" style="left:318px;top:248px">Click Here <svg viewBox="0 0 14 14"><path d="M2 7h10M8 3l4 4-4 4" stroke="#fff" stroke-width="1.6" fill="none"/></svg></a>
</section>
<section class="split promise">
  <div class="oval-photo" style="left:33px;background:linear-gradient(160deg,#3a4660,#c9a58e 55%,#e8d7c9)" role="img" aria-label="Photo of hands holding each other in support"></div>
  <h3 style="left:229px;top:94px">Our Patient Promise</h3>
  <p style="left:229px;top:126px">We promise to be there for you every step of your journey. Our goal is to help you grow from your struggles, heal from you pain, and move forward to where you want to be in your life.</p>
  <a class="btn teal" style="left:229px;top:250px">Click Here <svg viewBox="0 0 14 14"><path d="M2 7h10M8 3l4 4-4 4" stroke="#fff" stroke-width="1.6" fill="none"/></svg></a>
</section>

<h2 class="section-title" style="top:2476px">Our Treatment Approach and Therapy</h2>
<span class="arrow-circle" style="left:84px;top:2637px"><svg viewBox="0 0 10 10"><path d="M6.5 1.5L3 5l3.5 3.5" stroke="#0f2a4a" stroke-width="1.4" fill="none"/></svg></span>
<span class="arrow-circle" style="left:1091px;top:2637px"><svg viewBox="0 0 10 10"><path d="M3.5 1.5L7 5 3.5 8.5" stroke="#0f2a4a" stroke-width="1.4" fill="none"/></svg></span>
<article class="approach-card" style="left:120px"><div class="photo" style="background:linear-gradient(160deg,#b7b3ad,#8e8a85)" role="img" aria-label="Photo of a person curled up on the floor"></div><h4>Trauma &amp; PTSD</h4></article>
<article class="approach-card" style="left:366px"><div class="photo" style="background:linear-gradient(160deg,#5a3f34,#2d3240)" role="img" aria-label="Photo of a pensive man sitting against a wall"></div><h4>Depression &amp; Anxiety</h4></article>
<article class="approach-card" style="left:609px"><div class="photo" style="background:linear-gradient(160deg,#d9cfc6,#c0855c 60%,#e5ddd4)" role="img" aria-label="Photo of two people holding hands"></div><h4>Relationships</h4></article>
<article class="approach-card" style="left:853px"><div class="photo" style="background:linear-gradient(160deg,#ebe8e2,#8b9a78 60%,#d6d2cb)" role="img" aria-label="Photo of a therapy session in a bright room"></div><h4>Psychodynamic Therapy</h4></article>
<a class="btn" style="left:511px;top:2804px">View All Treatment <svg viewBox="0 0 14 14"><path d="M2 7h10M8 3l4 4-4 4" stroke="#fff" stroke-width="1.6" fill="none"/></svg></a>

<div class="cta-pattern" role="img" aria-label="Soft decorative pattern band"></div>

<footer class="footer">
  <div class="footer-col" style="left:120px;width:200px">
    <div style="display:flex;align-items:center;gap:8px;font-family:'Lexend',sans-serif;font-size:18px;line-height:21px;font-weight:500;color:#fff"><span style="width:10px;height:10px;border-radius:50%;background:var(--orange);flex:none"></span><span>Velora Health<br>Services</span></div>
    <p style="font-size:9.5px;line-height:13px;margin-top:20px">At Velora Health Services, we are committed to providing top-notch health consulting services to our clients Our mission is to help people achieve optimal health and wellness through personalized plans and ongoing support.</p>
    <div style="margin-top:18px"><span class="social"></span><span class="social"></span><span class="social"></span></div>
  </div>
  <span class="divider" style="left:331px"></span>
  <div class="footer-col" style="left:359px"><h4>Quick links</h4><ul><li>Home</li><li>About us</li><li>Therapies &amp; treatment</li><li>services</li><li>Gallery</li><li>Contact Us</li></ul></div>
  <span class="divider" style="left:499px"></span>
  <div class="footer-col" style="left:517px;width:190px"><h4>Contact Us</h4>
    <div class="contact-row"><span class="ic"><svg viewBox="0 0 12 12"><path d="M6 11S2 7 2 4.5a4 4 0 018 0C10 7 6 11 6 11z" stroke="#fff" fill="none"/><circle cx="6" cy="4.5" r="1.3" fill="#fff"/></svg></span>1847 Linden Court NW,<br>Suite 210 Washington, DC 20009</div>
    <div class="contact-row"><span class="ic"><svg viewBox="0 0 12 12"><path d="M3 1.5l2 2.5-1 1.2c.6 1.3 1.5 2.2 2.8 2.8L8 7l2.5 2-1 1.5C5.5 10.5 1.5 6.5 1.5 2.5z" fill="#fff"/></svg></span>202-555-0147</div>
    <div class="contact-row"><span class="ic"><svg viewBox="0 0 12 12"><rect x="2" y="4" width="8" height="5" rx="1" fill="#fff"/><rect x="3.5" y="2" width="5" height="2" fill="#fff"/></svg></span>202-555-0182</div>
    <div class="contact-row"><span class="ic"><svg viewBox="0 0 12 12"><rect x="1.5" y="3" width="9" height="6" stroke="#fff" fill="none"/><path d="M1.5 3L6 6.5 10.5 3" stroke="#fff" fill="none"/></svg></span><span style="color:#9fdadb">info@velorahealth.example</span></div>
  </div>
  <span class="divider" style="left:713px"></span>
  <div class="footer-col" style="left:736px"><h4>Opening Hours</h4>
    <div class="contact-row"><span class="ic"><svg viewBox="0 0 12 12"><circle cx="6" cy="6" r="4.5" stroke="#fff" fill="none"/><path d="M6 3.5V6h2" stroke="#fff" fill="none"/></svg></span>Mon to Fri<br>09:00 AM – 05:00 PM</div>
    <div class="contact-row"><span class="ic"><svg viewBox="0 0 12 12"><circle cx="6" cy="6" r="4.5" stroke="#fff" fill="none"/><path d="M6 3.5V6h2" stroke="#fff" fill="none"/></svg></span>Sat<br>10:00 AM – 02:00 PM</div>
    <div style="font-size:9.5px;margin-left:32px">Sun Closed</div>
  </div>
  <span class="divider" style="left:891px"></span>
  <div class="footer-col" style="left:911px"><h4>Subscribe Newsletter</h4>
    <div class="field">Enter Your Email</div>
    <a class="btn" style="position:relative;margin-top:18px;width:158px">Subscribe <svg viewBox="0 0 14 14"><path d="M2 7h10M8 3l4 4-4 4" stroke="#fff" stroke-width="1.6" fill="none"/></svg></a>
  </div>
  <div class="abs" style="left:120px;top:341px;width:960px;height:1px;background:#2d4566"></div>
  <div class="abs" style="left:115px;top:352px;font-size:9.5px">Copyright © 2025 Velora Health Services - All Rights Reserved.</div>
  <div class="abs" style="left:802px;top:352px;font-size:9.5px;word-spacing:2px">Terms and Conditions &nbsp; | &nbsp; Privacy Policy &nbsp; | &nbsp; Sitemap</div>
</footer>

<section class="cta">
  <h2>You Deserve to Feel Better—Let's Talk</h2>
  <p>We offer confidential, compassionate, and personalized care—because your<br>well-being is our priority. Reach out today and take the first step toward healing.</p>
  <a class="btn teal" style="left:253px;top:138px;width:146px">Call Us Today <svg viewBox="0 0 14 14"><path d="M2 7h10M8 3l4 4-4 4" stroke="#fff" stroke-width="1.6" fill="none"/></svg></a>
  <a class="btn white" style="left:408px;top:138px;width:146px">Get Started <svg viewBox="0 0 14 14"><path d="M2 7h10M8 3l4 4-4 4" stroke="#f47c20" stroke-width="1.6" fill="none"/></svg></a>
</section>

</body>
</html>
```